Deactivated Coal-Fired Power Plant to be redeveloped into a Green Energy Campus.

Want a striking business card statement that introduces our concept project to provide economic and community recovery to a former rural coal community in western PA.
Essentially 12 project representatives that will lead both the demolition of an existing power plant and the redevelopment to a new Green energy site.
Business Card should reflect our effort.
We are open to ideas.

Target Market(s)

Energy and Power Generation industries

Industry/Entity Type

Power Generation and Data Centers

Contact Information for Business Card

Included in uploaded materials

Font styles to use
Sans Serif
Other font styles liked:
• Arial, Calibri

Requirements
Must have
• Multiple colors

```html
<!DOCTYPE html>
<html lang="en">
<head>
<meta charset="utf-8">
<title>Ridgeline Renewal – Business Card</title>
<link href="https://fonts.googleapis.com/css2?family=Montserrat:wght@500;600;700&family=Arimo:wght@400;700&display=swap" rel="stylesheet">
<style>
  :root {
    --backdrop: #1b1b1c;
    --card: #333335;
    --green: #1f9e4a;
    --white: #ffffff;
    --muted: #e6e6e6;
    --divider: #6a6a6c;
  }
  * { box-sizing: border-box; margin: 0; padding: 0; }
  html, body { width: 1200px; height: 874px; overflow: hidden; }
  body {
    background: var(--backdrop);
    display: flex;
    flex-direction: column;
    align-items: center;
    justify-content: center;
    gap: 44px;
    font-family: "Arimo", Arial, sans-serif;
  }
  .card {
    width: 580px;
    height: 330px;
    background: var(--card);
    border-radius: 22px;
    position: relative;
    overflow: hidden;
  }
  /* Front */
  .card-front {
    display: flex;
    flex-direction: column;
    align-items: center;
    justify-content: center;
  }
  .brand {
    display: flex;
    align-items: center;
    gap: 14px;
  }
  .brand-dot {
    border-radius: 50%;
    background: var(--green);
    flex: none;
  }
  .brand-name {
    font-family: "Montserrat", sans-serif;
    font-weight: 700;
    color: var(--white);
    text-transform: uppercase;
    line-height: 1.05;
  }
  .card-front .brand-dot { width: 58px; height: 58px; }
  .card-front .brand-name { font-size: 40px; letter-spacing: 1px; }
  .tagline {
    margin-top: 34px;
    font-family: "Montserrat", sans-serif;
    font-weight: 600;
    font-size: 15px;
    letter-spacing: 2.5px;
    color: var(--white);
  }
  .tagline .accent { color: var(--green); }
  /* Back */
  .card-back {
    display: flex;
    align-items: center;
    padding: 0 34px 14px 36px;
  }
  .card-back::after {
    content: "";
    position: absolute;
    left: 0; right: 0; bottom: 0;
    height: 16px;
    background: var(--green);
  }
  .card-back .brand { width: 230px; gap: 10px; }
  .card-back .brand-dot { width: 36px; height: 36px; }
  .card-back .brand-name { font-size: 25px; }
  .divider {
    width: 1px;
    height: 150px;
    background: var(--divider);
    margin: 0 24px 0 10px;
  }
  .contact { color: var(--muted); }
  .person-name {
    font-weight: 700;
    font-size: 25px;
    color: var(--green);
  }
  .person-title { font-size: 15px; margin-top: 3px; }
  .company { font-size: 15px; margin-top: 8px; }
  .contact-list { list-style: none; margin-top: 12px; }
  .contact-list li {
    display: flex;
    align-items: center;
    gap: 9px;
    font-size: 15px;
    line-height: 21px;
  }
  .contact-list svg { width: 12px; height: 12px; flex: none; }
</style>
</head>
<body>
  <section class="card card-front">
    <div class="brand">
      <span class="brand-dot"></span>
      <span class="brand-name">Ridgeline Renewal</span>
    </div>
    <p class="tagline">YOUR <span class="accent">TAGLINE</span> HERE</p>
  </section>

  <section class="card card-back">
    <div class="brand">
      <span class="brand-dot"></span>
      <span class="brand-name">Ridgeline<br>Renewal</span>
    </div>
    <span class="divider"></span>
    <div class="contact">
      <p class="person-name">Daniel Marsh</p>
      <p class="person-title">Chief Operation Officer</p>
      <p class="company">Ridgeline Renewal LLC</p>
      <ul class="contact-list">
        <li>
          <svg viewBox="0 0 12 12" aria-hidden="true"><rect x="3" y="0.5" width="6" height="11" rx="1.2" fill="none" stroke="#1f9e4a" stroke-width="1.2"/><circle cx="6" cy="9.6" r="0.7" fill="#1f9e4a"/></svg>
          555.014.2280
        </li>
        <li>
          <svg viewBox="0 0 12 12" aria-hidden="true"><rect x="0.5" y="2.5" width="11" height="7" fill="#1f9e4a"/><path d="M0.5 2.5 L6 6.5 L11.5 2.5" fill="none" stroke="#333335" stroke-width="1"/></svg>
          dmarsh@ridgelinerenewal.com
        </li>
        <li>
          <svg viewBox="0 0 12 12" aria-hidden="true"><circle cx="6" cy="6" r="5.5" fill="#1f9e4a"/><path d="M0.5 6 H11.5 M6 0.5 C3 3.5 3 8.5 6 11.5 M6 0.5 C9 3.5 9 8.5 6 11.5" fill="none" stroke="#333335" stroke-width="0.8"/></svg>
          www.ridgelinerenewal.com
        </li>
      </ul>
    </div>
  </section>
</body>
</html>
```